Strategy and Technology Consulting - Our Story and Values Page

Interior Page design – Our History and Our Values

Our homepage has been designed and we are looking for a design for one of the interior pages. This interior page tells the story of Our History and Our Values

Because the homepage has been designed, we would like this interior page to reflect the design of the homepage without being a mirror image of the homepage.

This site will be implemented in WordPress using the Elementor framework.

Font: Poppins medium and Poppins dark
Illustrations: Our homepage illustrations were designed by “Teslo 1964” on Imagevale. Compatible original or stock illustrations are welcome. Stock photography is also welcome. Teslo is also available through Teslo Bramen on Portvue

• Homepage design – this is the design we will use for our homepage. Contest entries should reflect this basic style but should be distinctly different from the homepage.
• Our History and Our Values – Wireframe – the basic layout of the page we are looking for.
• Our History and Our Values – Word document with the text supporting the wireframe.
• Color Palette – please use colors compatible with the palette attached.

Our Story - timeline
There is a timeline element in the wireframe. The wireframe displays this as a series of chevrons (arrows), but it does not need to be. Creativity in display of the timeline is appreciated.

Our Values
If you look at the Word document, you will see that there are a lot of words on the page. The winning design will present the information in a way that engages the user without overwhelming them with too much to read. For example, they may click on a value and see more information.

Target Market(s)

CIO's and Technology Executives

Number of Pages Required

1 page

Font styles to use
Sans Serif
Other font styles liked:
• Poppin

Requirements
Must have
• A timeline element, all of our values
Nice to have
• Clever timeline display

```html
<!DOCTYPE html>
<html lang="en">
<head>
<meta charset="utf-8">
<title>Our Story and Values</title>
<link href="https://fonts.googleapis.com/css2?family=Poppins:wght@400;500;600;700;800&display=swap" rel="stylesheet">
<style>
  :root {
    --slate: #44546a;
    --gold: #e1b913;
    --blue: #236192;
    --mist: #f1f2f4;
    --white: #ffffff;
    --body-text: #3f4b5c;
  }
  * { margin: 0; padding: 0; box-sizing: border-box; }
  html, body { width: 754px; height: 1200px; overflow: hidden; background: var(--white); }
  body { font-family: "Poppins", sans-serif; color: var(--slate); }
  .page {
    position: relative;
    width: 1440px;
    height: 2292px;
    transform: scale(0.523611);
    transform-origin: 0 0;
    background: var(--white);
  }
  .page > * { position: absolute; }
  .story-backdrop { left: 0; top: 0; width: 1440px; height: 700px; }
  .page-title {
    left: 0; width: 1440px; top: 82px;
    text-align: center; font-size: 62px; font-weight: 800; letter-spacing: -0.5px;
  }
  .breadcrumb {
    left: 0; width: 1440px; top: 164px;
    text-align: center; font-size: 15px; font-weight: 500; letter-spacing: 1.5px;
  }
  .breadcrumb .current { color: #8a93a0; font-weight: 400; }
  .timeline-graphic { left: 0; top: 280px; width: 1440px; height: 500px; }
  .era-label {
    top: 287px; height: 44px; color: var(--white);
    font-size: 30px; font-weight: 700; line-height: 46px; text-align: center;
  }
  .era-one { left: 229px; width: 222px; background: var(--slate); }
  .era-two { left: 609px; width: 222px; background: var(--gold); }
  .era-three { left: 951px; width: 299px; background: var(--blue); }
  .era-points {
    top: 518px; width: 330px; list-style: none; color: var(--white);
    font-size: 15px; font-weight: 500; letter-spacing: 1.1px; line-height: 28px;
  }
  .era-points li { position: relative; padding-left: 19px; margin-bottom: 3px; }
  .era-points li::before {
    content: ""; position: absolute; left: 0; top: 10px;
    width: 8px; height: 8px; border-radius: 50%; background: var(--white);
  }
  .era-points li.sub { padding-left: 40px; margin-bottom: 0; }
  .era-points li.sub::before {
    left: 22px; top: 14px; width: 7px; height: 1px; border-radius: 0;
  }
  .points-one { left: 181px; }
  .points-two { left: 561px; }
  .points-three { left: 941px; }
  .values-title { left: 140px; top: 872px; font-size: 62px; font-weight: 800; letter-spacing: -0.5px; }
  .value-row { left: 0; width: 1440px; height: 166px; }
  .value-tab { position: absolute; left: 150px; top: 0; width: 400px; height: 140px; }
  .value-name {
    position: absolute; left: 196px; top: 0; height: 125px; width: 290px;
    display: flex; align-items: center;
    font-size: 19px; font-weight: 600; letter-spacing: 1.6px; line-height: 29px;
  }
  .value-row.is-active .value-name { color: var(--white); font-weight: 700; }
  .value-text {
    position: absolute; left: 611px; top: 2px; width: 705px;
    font-size: 16px; line-height: 31px; letter-spacing: 0.4px; color: var(--body-text);
  }
  .value-text .initial { font-size: 34px; line-height: 20px; font-weight: 400; color: var(--slate); }
</style>
</head>
<body>
<main class="page">
  <svg class="story-backdrop" viewBox="0 0 1440 700" aria-hidden="true">
    <path d="M0 0H1440V590C1340 560 1250 555 1150 570C900 610 500 660 150 638C80 633 30 615 0 595Z" fill="var(--mist)"/>
  </svg>

  <h1 class="page-title">Our Story</h1>
  <p class="breadcrumb">Home&gt;&gt;<span class="current">Our-Story</span></p>

  <svg class="timeline-graphic" viewBox="0 280 1440 500" aria-hidden="true">
    <g stroke="var(--slate)" stroke-width="1.5" stroke-dasharray="4 4" fill="none">
      <line x1="451" y1="311" x2="609" y2="311"/>
      <line x1="831" y1="311" x2="951" y2="311"/>
      <line x1="340" y1="331" x2="340" y2="404"/>
      <line x1="720" y1="331" x2="720" y2="404"/>
      <line x1="1100" y1="331" x2="1100" y2="404"/>
    </g>
    <polygon points="340,418 530,472 530,708 340,768 150,708 150,472" fill="var(--slate)"/>
    <polygon points="720,418 910,472 910,708 720,768 530,708 530,472" fill="var(--gold)"/>
    <polygon points="1100,418 1290,472 1290,708 1100,768 910,708 910,472" fill="var(--blue)"/>
    <g fill="var(--white)" stroke="var(--slate)" stroke-width="1.5" stroke-dasharray="3 3">
      <circle cx="340" cy="417" r="13"/>
      <circle cx="720" cy="417" r="13"/>
      <circle cx="1100" cy="417" r="13"/>
    </g>
  </svg>

  <div class="era-label era-one">2017 – 2019</div>
  <div class="era-label era-two">2020 – 2021</div>
  <div class="era-label era-three">2022 And Onward</div>

  <ul class="era-points points-one">
    <li>Growth Strategy Focus</li>
    <li>Consistent, Modest Growth</li>
    <li>Preliminary Focus on Technology</li>
    <li>Eureka!&nbsp; Implementing strategy is hard .</li>
  </ul>
  <ul class="era-points points-two">
    <li>Pandemic Pauses Growth</li>
    <li>Rethinking</li>
    <li class="sub">the business model</li>
    <li class="sub">the delivery model</li>
  </ul>
  <ul class="era-points points-three">
    <li>Leadership Team for Focus on Essential Areas</li>
    <li>Rapid Growth</li>
    <li>Customer Success</li>
  </ul>

  <h2 class="values-title">Our Values</h2>

  <section class="value-row is-active" style="top:1025px">
    <svg class="value-tab" viewBox="150 0 400 140" aria-hidden="true">
      <polygon points="158,0 490,0 527,62 490,125 158,125" fill="var(--gold)"/>
      <polyline points="492,0 530,62 492,125" fill="none" stroke="var(--blue)" stroke-width="5"/>
    </svg>
    <h3 class="value-name">The Value of Every Human.&nbsp; Regardless.</h3>
    <p class="value-text"><span class="initial">E</span>ach person's unique experiences and perspectives add vibrant hues to the tapestry of our shared existence.&nbsp; In a world where diversity paints the canvas of humanity, true beauty is found in recognizing the inherent and incalculable value of every human being.</p>
  </section>

  <section class="value-row" style="top:1191px">
    <svg class="value-tab" viewBox="150 0 400 140" aria-hidden="true">
      <polygon points="158,0 490,0 527,62 490,125 158,125" fill="var(--white)" style="filter:drop-shadow(0 4px 6px rgba(68,84,106,.08))"/>
      <polyline points="492,0 530,62 492,125" fill="none" stroke="var(--gold)" stroke-width="5"/>
    </svg>
    <h3 class="value-name">Collaboration</h3>
    <p class="value-text"><span class="initial">C</span>ollaboration in work transforms individual endeavors into symphonies of collective achievement. Through collaboration, diverse talents converge, fostering a rich exchange of ideas that amplifies creativity, accelerates progress, and brings forth solutions beyond what a single mind could conceive.</p>
  </section>

  <section class="value-row" style="top:1357px">
    <svg class="value-tab" viewBox="150 0 400 140" aria-hidden="true">
      <polygon points="158,0 490,0 527,62 490,125 158,125" fill="var(--white)" style="filter:drop-shadow(0 4px 6px rgba(68,84,106,.08))"/>
      <polyline points="492,0 530,62 492,125" fill="none" stroke="var(--gold)" stroke-width="5"/>
    </svg>
    <h3 class="value-name">Passion</h3>
    <p class="value-text"><span class="initial">P</span>assion infuses our work with energy, transforming routine tasks into opportunities for creativity and innovation. Fueled by passion, individuals become unstoppable forces, driven to overcome challenges and achieve remarkable outcomes that benefit them and inspire those around them</p>
  </section>

  <section class="value-row" style="top:1523px">
    <svg class="value-tab" viewBox="150 0 400 140" aria-hidden="true">
      <polygon points="158,0 490,0 527,62 490,125 158,125" fill="var(--white)" style="filter:drop-shadow(0 4px 6px rgba(68,84,106,.08))"/>
      <polyline points="492,0 530,62 492,125" fill="none" stroke="var(--gold)" stroke-width="5"/>
    </svg>
    <h3 class="value-name">Excellence</h3>
    <p class="value-text"><span class="initial">E</span>xcellence isn't a destination; it's a continuous journey of refinement and growth. Striving for excellence cultivates a culture of continuous improvement, fostering innovation, credibility, and a lasting impact that resonates far beyond the immediate task.</p>
  </section>

  <section class="value-row" style="top:1689px">
    <svg class="value-tab" viewBox="150 0 400 140" aria-hidden="true">
      <polygon points="158,0 490,0 527,62 490,125 158,125" fill="var(--white)" style="filter:drop-shadow(0 4px 6px rgba(68,84,106,.08))"/>
      <polyline points="492,0 530,62 492,125" fill="none" stroke="var(--gold)" stroke-width="5"/>
    </svg>
    <h3 class="value-name">Tenacity</h3>
    <p class="value-text"><span class="initial">T</span>enacity is the unwavering anchor that keeps us grounded amidst adversity, propelling us forward when faced with obstacles. The resilience to persist, adapt, and learn from setbacks leads to the mastery of skills and the fulfillment of ambitious goals.</p>
  </section>

  <section class="value-row" style="top:1855px">
    <svg class="value-tab" viewBox="150 0 400 140" aria-hidden="true">
      <polygon points="158,0 490,0 527,62 490,125 158,125" fill="var(--white)" style="filter:drop-shadow(0 4px 6px rgba(68,84,106,.08))"/>
      <polyline points="492,0 530,62 492,125" fill="none" stroke="var(--gold)" stroke-width="5"/>
    </svg>
    <h3 class="value-name">Solution Mindset</h3>
    <p class="value-text"><span class="initial">A</span> solution mindset is the compass that directs our focus from problems to possibilities. It empowers us to navigate challenges with a proactive mindset, igniting a journey of exploration and innovation that not only resolves issues but also paves the way for continuous growth and success.</p>
  </section>

  <section class="value-row" style="top:2021px">
    <svg class="value-tab" viewBox="150 0 400 140" aria-hidden="true">
      <polygon points="158,0 490,0 527,62 490,125 158,125" fill="var(--white)" style="filter:drop-shadow(0 4px 6px rgba(68,84,106,.08))"/>
      <polyline points="492,0 530,62 492,125" fill="none" stroke="var(--gold)" stroke-width="5"/>
    </svg>
    <h3 class="value-name">Generosity</h3>
    <p class="value-text"><span class="initial">G</span>enerosity creates a virtuous cycle of goodwill, fostering a sense of unity and shared purpose among colleagues. By freely sharing knowledge, support, and resources, we uplift those around us and contribute to a collaborative environment where collective achievements flourish.</p>
  </section>
</main>
</body>
</html>
```